KLT-AZ Presentation Folder

The old design is attached. We're looking to revamp our Arizona offices with a fresh new look.

Front Cover

The Company Logo is prominently displayed.
Tagline: "Improving Homes. Improving Lives."
Image of a beautiful home showcasing new windows and doors
Website: crestfieldpaneworksaz.example
Social media icons: Chatterloop, Snapvale, ClipDrome, Rateburrow
Mention: "Follow us for the latest updates and tips."

Back Cover

Thank You Message: "Thank you for choosing Crestfield Pane Works. We appreciate your trust in us to improve your home."
Contact Information:
Customer Service: 480.555.0187
Call Center: 480.555.0143
ROC License Number: #418302
Additional social media handles and website details.
Small disclaimer or legal note if necessary.

Inside Left Panel

Photo of Doug and Marian Solvik (founders)
Short blurb/quote: “Our mission is to provide the best window and door solutions with a personal touch. Thank you for letting us be a part of your home improvement journey.”
Slots for business cards (either sales or customer service rep)

Inside Right Panel

Thank You Message: “We’re honored to be a part of your home transformation. Our commitment to quality and customer satisfaction ensures you receive the best service and products.”
List of Services (e.g., window and door installations, energy-efficient solutions)
Highlight the company’s QTC accreditation A+

Encourage the customer to reach out if they need further assistance or have any questions, with a reminder of the contact details.

https://www.qtcreview.example/us/az/gilbert/profile/home-improvement/crestfield-pane-works-4471-2000058314

https://crestfieldpaneworksaz.example/

We need thirty more days to decide.

Gathering more feedback

Designs look the same

```html
<!DOCTYPE html>
<html lang="en">
<head>
<meta charset="utf-8">
<title>Crestfield Pane Works Presentation Folder</title>
<link href="https://fonts.googleapis.com/css2?family=Montserrat:wght@400;500;600;700&family=Zilla+Slab:ital,wght@1,700&display=swap" rel="stylesheet">
<style>
  :root{
    --navy:#1b2757;
    --navy-deep:#141d45;
    --navy-soft:#26336a;
    --teal:#5ec8d8;
    --green:#6dbf4b;
    --white:#ffffff;
    --paper:#ffffff;
    --stage:#e4e4e4;
    --muted:#c9d1e8;
  }
  *{box-sizing:border-box;margin:0;padding:0}
  html,body{width:782px;height:1200px;overflow:hidden;background:var(--stage)}
  body{position:relative;font-family:"Montserrat",sans-serif;color:var(--white)}

  .spread{position:absolute;left:81px;width:625px;height:405px;box-shadow:0 2px 6px rgba(0,0,0,.25)}
  .spread--outside{top:150px;background:linear-gradient(160deg,var(--navy-soft) 0%,var(--navy) 45%,var(--navy-deep) 100%)}
  .spread--inside{top:655px;background:var(--paper)}

  .abs{position:absolute;white-space:nowrap}
  .flap-notch{position:absolute;left:0;top:0}

  .thanks-head{left:19px;top:69px;font-size:9.4px;font-weight:500;letter-spacing:-.15px;color:var(--teal)}
  .brand{display:flex;align-items:center;gap:5px;font-weight:700;color:var(--white);line-height:1.1;white-space:normal}
  .brand__mark{width:10px;height:10px;background:var(--teal);flex:none}
  .brand--small{left:20px;top:92px;width:100px;font-size:9px}
  .brand--cover{left:508px;top:66px;width:100px;font-size:9.5px}
  .brand--pocket{left:362px;top:300px;width:110px;font-size:11px}
  .appreciate{left:19px;top:143px;width:120px;font-size:7.3px;font-weight:500;line-height:1.35;white-space:normal}

  .call-now{left:19px;top:272px;font-size:7.5px;font-weight:700;color:var(--teal)}
  .call-sub{left:19px;top:282px;font-size:6.1px;line-height:1.4;color:var(--muted)}
  .rule{height:1px;background:var(--teal)}
  .rule--contact{left:19px;top:305px;width:107px;opacity:.7}
  .contact{left:18px;display:flex;align-items:center;gap:3px;font-size:5.4px;letter-spacing:-.1px}
  .contact strong{font-size:6.8px;font-weight:700;letter-spacing:-.1px}
  .contact--service{top:310px}
  .contact--center{top:322px}
  .contact--web{top:335px}
  .icon{width:9px;height:9px;flex:none}

  .follow{font-size:4.8px;font-weight:500}
  .follow--back{left:19px;top:370px}
  .follow--cover{left:509px;top:370px}
  .socials{display:flex;gap:2.5px}
  .socials--back{left:19px;top:379px}
  .socials--cover{left:509px;top:379px}
  .social{width:9px;height:9px;border:1px solid var(--white);border-radius:50%}

  .license{left:141px;top:383px;font-size:4.8px}
  .license strong{font-weight:700}

  .photo{position:absolute;border-radius:6px}
  .photo--loft{left:144px;top:42px;width:158px;height:161px;background:linear-gradient(160deg,#e9e9e6,#7b7d78 60%,#2f302d)}
  .photo--living{left:322px;top:42px;width:161px;height:162px;background:linear-gradient(170deg,#f1ede4,#c7c2b2 55%,#8c8572)}
  .photo--hall{left:141px;top:216px;width:162px;height:162px;background:linear-gradient(170deg,#f4f1ea,#9f8a6f 50%,#e8e4dc)}
  .photo--patio{left:322px;top:216px;width:161px;height:162px;background:linear-gradient(175deg,#8fb1d8,#5c5a52 45%,#8a7c68 75%,#3e6b35)}

  .cover-web{left:508px;top:114px;display:flex;align-items:center;gap:3px;font-size:5px}
  .cover-web .icon{width:7px;height:7px}

  .tagline{left:509px;top:202px;font-size:15.5px;line-height:1.33;letter-spacing:.4px}
  .tagline .strong{font-weight:700;color:var(--teal)}
  .tagline .light{font-weight:400;color:var(--white)}

  .fold{left:312px;top:0;width:1px;height:405px;background:#e6e6e6}
  .pocket{position:absolute;top:280px;height:125px;background:linear-gradient(170deg,var(--navy-soft),var(--navy) 60%,var(--navy-deep))}
  .pocket--left{left:0;width:312px;clip-path:polygon(0 0,300px 0,312px 100%,0 100%)}
  .pocket--right{left:312px;width:313px;clip-path:polygon(13px 0,100% 0,100% 100%,0 100%)}

  .founder-photo{left:26px;top:292px;width:86px;height:86px;border-radius:50%;border:2px solid var(--green);background:linear-gradient(160deg,#d9c98f,#caa57b 50%,#f2f2f2)}
  .quote-mark{left:105px;top:284px;font-size:36px;line-height:1;font-weight:700;color:var(--teal);font-family:"Zilla Slab",serif;font-style:italic}
  .founders-name{left:123px;top:307px;font-family:"Zilla Slab",serif;font-style:italic;font-weight:700;font-size:10.5px;color:var(--teal)}
  .founders-role{left:123px;top:322px;font-size:5.3px}
  .founders-quote{left:123px;top:332px;width:134px;font-size:5.8px;letter-spacing:-.1px;line-height:1.45;white-space:normal}
  .rule--founders{left:123px;top:375px;width:126px;background:var(--green)}

  .honored{left:486px;top:290px;width:122px;font-size:5.6px;line-height:1.4;color:var(--teal);white-space:normal}
  .services-head{left:486px;top:326px;font-family:"Zilla Slab",serif;font-style:italic;font-weight:700;font-size:8px;color:var(--teal);text-decoration:underline}
  .services{left:486px;top:338px;list-style:none;font-size:5.4px;font-weight:700;line-height:1.5}
  .services li::before{content:"";display:inline-block;width:2.5px;height:2.5px;border-radius:50%;background:var(--teal);margin-right:3px;vertical-align:middle}
  .rule--services{left:486px;top:367px;width:114px;opacity:.8}
  .badge{left:370px;top:371px;width:24px;height:15px;border:1px solid var(--white);border-radius:2px;background:var(--navy-soft)}
  .disclaimer{left:406px;top:373px;width:140px;font-size:3.6px;line-height:1.4;color:var(--muted);white-space:normal}
</style>
</head>
<body>

<section class="spread spread--outside" aria-label="Folder outside: back cover and front cover">
  <svg class="flap-notch" width="625" height="40" viewBox="0 0 625 40" aria-hidden="true">
    <path d="M106 0 H519 L561 35 Q563 38 559 38 H64 Q60 38 63 35 Z" fill="#ffffff"/>
  </svg>

  <p class="abs thanks-head">Thank you for choosing</p>
  <div class="abs brand brand--small"><span class="brand__mark"></span>Crestfield Pane Works</div>
  <p class="abs appreciate">We appreciate your trust in us to improve your home.</p>

  <p class="abs call-now">CALL NOW</p>
  <p class="abs call-sub">for further assistance or<br>if you have any questions:</p>
  <div class="abs rule rule--contact"></div>

  <p class="abs contact contact--service">
    <svg class="icon" viewBox="0 0 10 10" aria-hidden="true"><circle cx="5" cy="5" r="4.4" fill="none" stroke="#fff" stroke-width=".7"/><circle cx="5" cy="4" r="1.3" fill="#fff"/><path d="M2.8 7.3 Q5 5 7.2 7.3" fill="none" stroke="#fff" stroke-width=".8"/></svg>
    Customer Service: <strong>480.555.0187</strong>
  </p>
  <p class="abs contact contact--center">
    <svg class="icon" viewBox="0 0 10 10" aria-hidden="true"><circle cx="5" cy="5" r="4.4" fill="none" stroke="#fff" stroke-width=".7"/><path d="M3.4 2.8 L4.3 2.6 L4.7 3.9 L4.1 4.4 Q4.7 5.6 5.7 6 L6.2 5.4 L7.4 5.8 L7.2 6.7 Q5.6 7.3 4.1 5.9 Q2.9 4.5 3.4 2.8 Z" fill="#fff"/></svg>
    Call Center: <strong>480.555.0143</strong>
  </p>
  <p class="abs contact contact--web">
    <svg class="icon" viewBox="0 0 10 10" aria-hidden="true"><circle cx="5" cy="5" r="4.4" fill="none" stroke="#fff" stroke-width=".7"/><circle cx="5" cy="5" r="2.6" fill="none" stroke="#fff" stroke-width=".5"/><path d="M2.4 5 H7.6 M5 2.4 V7.6" stroke="#fff" stroke-width=".5"/></svg>
    crestfieldpaneworksaz.example
  </p>

  <p class="abs follow follow--back">Follow us for the latest updates and tips.</p>
  <div class="abs socials socials--back">
    <span class="social" aria-label="Chatterloop"></span>
    <span class="social" aria-label="Snapvale"></span>
    <span class="social" aria-label="ClipDrome"></span>
    <span class="social" aria-label="Rateburrow"></span>
  </div>

  <div class="photo photo--loft" role="img" aria-label="Bright loft living room with tall black-framed windows"></div>
  <div class="photo photo--living" role="img" aria-label="Living room with large white-framed windows and garden view"></div>
  <div class="photo photo--hall" role="img" aria-label="High-ceiling room with tall wood-framed window wall"></div>
  <div class="photo photo--patio" role="img" aria-label="Home patio at dusk with new glass doors and windows"></div>
  <p class="abs license">ROC License Number: <strong>#418302</strong></p>

  <div class="abs brand brand--cover"><span class="brand__mark"></span>Crestfield Pane Works</div>
  <p class="abs cover-web">
    <svg class="icon" viewBox="0 0 10 10" aria-hidden="true"><circle cx="5" cy="5" r="4.4" fill="none" stroke="#fff" stroke-width=".7"/><path d="M2.4 5 H7.6 M5 2.4 V7.6" stroke="#fff" stroke-width=".5"/></svg>
    crestfieldpaneworksaz.example
  </p>

  <p class="abs tagline">
    <span class="strong">IMPROVING</span><br>
    <span class="light">HOMES.</span><br>
    <span class="strong">IMPROVING</span><br>
    <span class="light">LIVES.</span>
  </p>

  <p class="abs follow follow--cover">Follow us for the latest updates and tips.</p>
  <div class="abs socials socials--cover">
    <span class="social" aria-label="Chatterloop"></span>
    <span class="social" aria-label="Snapvale"></span>
    <span class="social" aria-label="ClipDrome"></span>
    <span class="social" aria-label="Rateburrow"></span>
  </div>
</section>

<section class="spread spread--inside" aria-label="Folder inside with pockets">
  <div class="abs fold"></div>

  <div class="pocket pocket--left"></div>
  <div class="abs founder-photo" role="img" aria-label="Portrait of founders Doug and Marian Solvik"></div>
  <p class="abs quote-mark">“</p>
  <p class="abs founders-name">Doug &amp; Marian Solvik</p>
  <p class="abs founders-role">Founders</p>
  <p class="abs founders-quote">Our mission is to provide the best window and door solutions with a personal touch. Thank you for letting us be a part of your home improvement journey.”</p>
  <div class="abs rule rule--founders"></div>

  <div class="pocket pocket--right"></div>
  <div class="abs brand brand--pocket"><span class="brand__mark"></span>Crestfield Pane Works</div>
  <p class="abs honored">We’re honored to be a part of your home transformation. Our commitment to quality and customer satisfaction ensures you receive the best service and products.</p>
  <p class="abs services-head">SERVICES</p>
  <ul class="abs services">
    <li>Window &amp; Door Installations</li>
    <li>Window &amp; Door Replacement</li>
    <li>Energy-efficient Solutions</li>
  </ul>
  <div class="abs rule rule--services"></div>
  <div class="abs badge" role="img" aria-label="QTC A+ accreditation badge"></div>
  <p class="abs disclaimer">This business is in an industry that may require professional licensing, bonding or registration. QTC encourages you to check with the appropriate agency to be certain any requirements are currently being met.</p>
</section>

</body>
</html>
```